Landscaping flier 2024

Create a 1 page flier for landscaping services
1. Must be completed in Adobe Photoshop
2. Size 8.5" x 11" (portrait layout)
3. Include logo
4. Text to include:
2024 Gravesite Landscaping Packages
info@maplecrestmemorial.example
(201) 555-0148
maplecrestmemorial.example
5. Use chart text for the content. DO NOT COPY THE CHART DESIGN/FORMAT. Use the chart for the text you need only.
6. Use "Pricing cards as format for laying out the chart". Open to other ideas as well.
**Use the example of chart design (handwritten) to base your design off of.
7. Photos
-include before and after care photos

```html
<!DOCTYPE html>
<html lang="en">
<head>
<meta charset="utf-8">
<title>Maplecrest Memorial – 2024 Gravesite Landscaping Packages</title>
<link rel="stylesheet" href="https://fonts.googleapis.com/css2?family=Poppins:wght@400;500;600;700;800;900&family=Cinzel:wght@500;600&display=swap">
<style>
:root{
  --navy:#1f2d3d;
  --navy-deep:#17222f;
  --maroon:#7b1c26;
  --maroon-dark:#6a1520;
  --red-row:#a5303b;
  --gray-row:#dedede;
  --white:#ffffff;
  --paper:#f4f4f4;
  --check:#4f8a2b;
  --cross:#d9534f;
  --gold:#f2cf2b;
  --stage:#e9e9e9;
}
*{box-sizing:border-box;margin:0;padding:0}
html,body{width:1200px;height:2995px;overflow:hidden;background:var(--stage);font-family:"Poppins",sans-serif}
.flier{position:absolute;left:50px;top:786px;width:1100px;height:1423px;background:var(--paper);overflow:hidden;box-shadow:0 10px 40px rgba(0,0,0,.18)}
.hero{position:absolute;left:0;top:0;width:1100px;height:358px;background:linear-gradient(180deg,#2a3a4c 0%,var(--navy) 60%,#223143 100%)}
.brand-tab{position:absolute;left:216px;top:0;width:664px;height:132px;background:var(--white);clip-path:polygon(0 0,100% 0,92% 100%,8% 100%);border-radius:0 0 24px 24px;display:flex;align-items:center;justify-content:center;gap:18px}
.brand-mark{width:64px;height:64px;border-radius:50%;border:3px solid var(--navy)}
.brand-name{font-family:"Cinzel",serif;font-weight:600;font-size:40px;color:var(--maroon);letter-spacing:1px}
.title{position:absolute;left:0;width:1100px;text-align:center;color:var(--white)}
.title-main{top:150px;font-family:"Poppins",sans-serif;font-weight:900;font-size:92px;letter-spacing:1px;line-height:1}
.title-sub{top:246px;font-family:"Cinzel",serif;font-weight:500;font-size:68px;line-height:1}
.pricelist-tab{position:absolute;left:0;top:358px;width:700px;height:0}
.pricelist-tab::before{content:"";position:absolute;left:0;top:-52px;width:660px;height:52px;background:var(--paper);clip-path:polygon(0 0,94% 0,100% 100%,0 100%)}
.pricelist-heading{position:absolute;left:80px;top:318px;font-weight:800;font-size:34px;color:var(--maroon);letter-spacing:.3px}
.card{position:absolute;top:414px;width:318px;border-radius:12px;overflow:hidden;display:flex;flex-direction:column;border:2px solid var(--maroon);background:var(--white)}
.card.seasonal{left:63px}
.card.basic{left:390px}
.card.perpetual{left:717px;top:382px;border-color:var(--navy)}
.card-head{height:84px;display:flex;align-items:center;justify-content:center;text-align:center;font-weight:800;font-size:26px;line-height:1.02;color:var(--maroon);background:var(--white)}
.perpetual .card-head{height:116px;padding-top:22px;color:var(--white);background:var(--navy);font-weight:600}
.card-desc{height:50px;display:flex;align-items:center;justify-content:center;text-align:center;font-size:13px;line-height:1.2;color:var(--white);background:var(--maroon);padding:0 30px}
.perpetual .card-desc{background:var(--red-row);color:#f5d7da}
.row{display:flex;align-items:center;gap:14px;padding:0 12px 0 22px;font-weight:500;font-size:15.5px;line-height:1.2;color:#3b4552}
.row .txt small{display:block;font-weight:400;font-size:13px;line-height:1.15;margin-top:3px}
.row svg{flex:none;width:24px;height:24px}
.row.weeding{height:110px;align-items:flex-start;padding-top:14px}
.r-monument{height:44px}.r-payment{height:63px}.r-boxwood{height:65px}.r-replace{height:44px}.r-trust{height:44px}
.seasonal .row:nth-of-type(odd),.basic .row:nth-of-type(odd){background:var(--gray-row)}
.seasonal .row.weeding,.basic .row.weeding{background:var(--white)}
.seasonal .r-monument,.basic .r-monument,.seasonal .r-boxwood,.basic .r-boxwood,.seasonal .r-trust,.basic .r-trust{background:var(--gray-row)}
.seasonal .r-payment,.basic .r-payment,.seasonal .r-replace,.basic .r-replace{background:var(--white)}
.perpetual .row{color:var(--white);font-weight:600}
.perpetual .row.weeding,.perpetual .r-payment,.perpetual .r-replace{background:var(--maroon-dark)}
.perpetual .r-monument,.perpetual .r-boxwood,.perpetual .r-trust{background:var(--red-row)}
.price{position:relative;height:129px;background:var(--navy);color:var(--white);text-align:center}
.price-label{padding-top:10px;font-size:13px;letter-spacing:.2px}
.price-amount{font-weight:600;font-size:48px;line-height:1.1}
.price-amount sup{font-size:22px;vertical-align:top;position:relative;top:8px}
.terms{display:flex;justify-content:space-around;padding:10px 14px 0;font-size:13px}
.terms div{display:flex;flex-direction:column;align-items:center}
.terms b{font-weight:600;font-size:34px;line-height:1.15}
.terms b sup{font-size:17px;vertical-align:top;position:relative;top:4px}
.price-note{position:absolute;left:40px;right:40px;bottom:-2px;height:44px;background:var(--white);border-radius:10px 10px 0 0;border:2px solid var(--navy);border-bottom:none;display:flex;align-items:center;justify-content:center;text-align:center;font-size:13px;line-height:1.15;color:#3b4552;padding:0 18px}
.ribbon{position:absolute;left:717px;top:382px;width:80px;height:80px;overflow:hidden;z-index:3}
.ribbon span{position:absolute;left:-32px;top:18px;width:130px;transform:rotate(-45deg);background:var(--gold);color:var(--navy);font-weight:700;font-size:10px;text-align:center;padding:3px 0;letter-spacing:.3px}
.valid{position:absolute;left:276px;top:1046px;width:536px;height:40px;background:var(--navy);border-radius:0 0 20px 20px;color:var(--white);font-weight:700;font-size:27px;text-align:center;line-height:40px;z-index:2}
.footer{position:absolute;left:0;top:1252px;width:1100px;height:171px;background:var(--maroon)}
.photo-frame{position:absolute;left:97px;top:1090px;width:906px;height:262px;background:var(--paper);border-radius:0 0 18px 18px}
.photo{position:absolute;top:1104px;width:388px;height:232px;border-radius:14px;overflow:hidden;background:linear-gradient(180deg,#7c8a6a 0%,#5f8a33 35%,#6da33a 70%,#4f7f2a 100%)}
.photo.before{left:161px}
.photo.after{left:561px;background:linear-gradient(180deg,#8b9577 0%,#5e8c35 35%,#71aa3d 72%,#55862c 100%)}
.photo-label{position:absolute;bottom:0;left:72px;width:244px;height:46px;background:var(--maroon);border-radius:22px 22px 0 0;color:var(--white);font-weight:700;font-size:26px;text-align:center;line-height:48px}
.contact{position:absolute;left:0;top:1355px;width:1100px;display:flex;justify-content:center;align-items:center;gap:42px;color:var(--white)}
.contact-item{display:flex;align-items:center;gap:8px;font-size:18px}
.contact-item.phone{font-size:28px}
.contact-item svg{width:22px;height:22px;fill:none;stroke:var(--white);stroke-width:2}
</style>
</head>
<body>
<main class="flier">
  <section class="hero">
    <div class="brand-tab">
      <span class="brand-mark"></span>
      <span class="brand-name">Maplecrest Memorial</span>
    </div>
    <h1 class="title title-main">2024 GRAVESITE</h1>
    <p class="title title-sub">Landscaping Packages</p>
  </section>

  <div class="pricelist-tab"></div>
  <h2 class="pricelist-heading">SERVICES OFFERED <span style="color:var(--navy)">PRICELIST</span></h2>

  <svg width="0" height="0" style="position:absolute">
    <defs>
      <symbol id="tick" viewBox="0 0 24 24"><path d="M3 12.5l6 6L21 5" fill="none" stroke="#4f8a2b" stroke-width="3" stroke-linecap="round" stroke-linejoin="round"/></symbol>
      <symbol id="cross" viewBox="0 0 24 24"><path d="M5 5l14 14M19 5L5 19" fill="none" stroke="#d9534f" stroke-width="2.4" stroke-linecap="round"/></symbol>
    </defs>
  </svg>

  <article class="card seasonal">
    <h3 class="card-head">SEASONAL<br>CARE</h3>
    <p class="card-desc">Seasonal landscaping grave care.</p>
    <div class="row weeding"><svg><use href="#tick"/></svg><span class="txt">WEEDING &amp; TRIMMING<br>ON YOUR GRAVESITE<small>Approximately every 7 weeks during the growing season: mid-April through mid-October</small></span></div>
    <div class="row r-monument"><svg><use href="#cross"/></svg><span class="txt">MONUMENT LEVELING</span></div>
    <div class="row r-payment"><svg><use href="#cross"/></svg><span class="txt">PAYMENT ENSURES<br>GRAVE CARE FOREVER</span></div>
    <div class="row r-boxwood"><svg><use href="#cross"/></svg><span class="txt">FULL BED OF BOXWOOD<br>SHRUBS</span></div>
    <div class="row r-replace"><svg><use href="#cross"/></svg><span class="txt">REPLACEMENT OF SHRUBS</span></div>
    <div class="row r-trust"><svg><use href="#cross"/></svg><span class="txt">TRUST CERTIFICATE</span></div>
    <div class="price">
      <div class="terms">
        <div>3 YEARS<b><sup>$</sup>396</b></div>
        <div>2 YEARS<b><sup>$</sup>264</b></div>
        <div>1 YEAR<b><sup>$</sup>132</b></div>
      </div>
      <p class="price-note">Multi-year payment locks in current rates</p>
    </div>
  </article>

  <article class="card basic">
    <h3 class="card-head">BASIC CARE<br>ENDOWMENT</h3>
    <p class="card-desc">Landscaping care forever for graves with no plantings.</p>
    <div class="row weeding"><svg><use href="#tick"/></svg><span class="txt">WEEDING &amp; TRIMMING<br>ON YOUR GRAVESITE<small>2 times per year: mid-May &amp; mid-September</small></span></div>
    <div class="row r-monument"><svg><use href="#tick"/></svg><span class="txt">MONUMENT LEVELING</span></div>
    <div class="row r-payment"><svg><use href="#tick"/></svg><span class="txt">PAYMENT ENSURES<br>GRAVE CARE FOREVER</span></div>
    <div class="row r-boxwood"><svg><use href="#tick"/></svg><span class="txt">FULL BED OF BOXWOOD<br>SHRUBS</span></div>
    <div class="row r-replace"><svg><use href="#tick"/></svg><span class="txt">REPLACEMENT OF SHRUBS</span></div>
    <div class="row r-trust"><svg><use href="#tick"/></svg><span class="txt">TRUST CERTIFICATE</span></div>
    <div class="price">
      <p class="price-label">12 MONTHLY PAYMENTS OF</p>
      <p class="price-amount"><sup>$</sup>287</p>
      <p class="price-note">Call for single payment discount.</p>
    </div>
  </article>

  <article class="card perpetual">
    <h3 class="card-head">PERPETUAL CARE<br>ENDOWMENT</h3>
    <p class="card-desc">Landscaping care forever for graves with plantings.</p>
    <div class="row weeding"><svg><use href="#tick"/></svg><span class="txt">WEEDING &amp; TRIMMING<br>ON YOUR GRAVESITE<small>Approximately every 7 weeks during the growing season: mid-April through mid-October</small></span></div>
    <div class="row r-monument"><svg><use href="#tick"/></svg><span class="txt">MONUMENT LEVELING</span></div>
    <div class="row r-payment"><svg><use href="#tick"/></svg><span class="txt">PAYMENT ENSURES<br>GRAVE CARE FOREVER</span></div>
    <div class="row r-boxwood"><svg><use href="#tick"/></svg><span class="txt">FULL BED OF BOXWOOD<br>SHRUBS</span></div>
    <div class="row r-replace"><svg><use href="#tick"/></svg><span class="txt">REPLACEMENT OF SHRUBS</span></div>
    <div class="row r-trust"><svg><use href="#tick"/></svg><span class="txt">TRUST CERTIFICATE</span></div>
    <div class="price">
      <p class="price-label">12 MONTHLY PAYMENTS OF</p>
      <p class="price-amount"><sup>$</sup>351</p>
      <p class="price-note">Call for single payment discount.</p>
    </div>
  </article>
  <div class="ribbon"><span>MOST POPULAR</span></div>

  <p class="valid">VALID THROUGH 10/31/2024</p>

  <footer class="footer"></footer>
  <div class="photo-frame"></div>
  <figure class="photo before" role="img" aria-label="Photo of an overgrown gravesite with tall grass and weeds before care">
    <figcaption class="photo-label">BEFORE CARE</figcaption>
  </figure>
  <figure class="photo after" role="img" aria-label="Photo of the same gravesite after care with trimmed boxwood shrubs and a level marker">
    <figcaption class="photo-label">AFTER CARE</figcaption>
  </figure>

  <div class="contact">
    <span class="contact-item phone"><svg viewBox="0 0 24 24"><path d="M5 3h4l2 5-2.5 1.5a11 11 0 0 0 6 6L16 13l5 2v4a2 2 0 0 1-2 2A17 17 0 0 1 3 5a2 2 0 0 1 2-2z"/></svg>(201) 555-0148</span>
    <span class="contact-item"><svg viewBox="0 0 24 24"><path d="M12 21s-7-6.5-7-12a7 7 0 0 1 14 0c0 5.5-7 12-7 12z"/><circle cx="12" cy="9" r="2.5"/></svg>48 Orchard Lane, Fairview, NJ 07000</span>
    <span class="contact-item"><svg viewBox="0 0 24 24"><circle cx="12" cy="12" r="9"/><path d="M3 12h18M12 3c3 3 3 15 0 18M12 3c-3 3-3 15 0 18"/></svg>www.maplecrestmemorial.example</span>
  </div>
</main>
</body>
</html>
```